Business card for partnership

Plumbing and hvac company needing a minimal business card. We already have a logo i would like the front of the card just the logo and the back have all info.

Target Market(s)

Commercial facilities

Industry/Entity Type

Plumbing hvac

Contact Information for Business Card

We would like it double sided. Logo big and bold on the front and out info on the back. Our info on back would be name and position phone, email, and location

```html
<!DOCTYPE html>
<html lang="en">
<head>
<meta charset="utf-8">
<title>Keystone Mechanical – Business Card</title>
<link rel="stylesheet" href="https://fonts.googleapis.com/css2?family=Arimo:wght@400;700&display=swap">
<style>
  :root {
    --backdrop: #cfcfcf;
    --card-white: #ffffff;
    --card-grey: #e8e8e8;
    --ink: #1d1d1d;
    --ink-logo: #333333;
    --accent: #f0842c;
    --edge: #d9141c;
    --divider: #d4d4d4;
  }
  * { box-sizing: border-box; margin: 0; padding: 0; }
  html, body {
    width: 1200px;
    height: 800px;
    overflow: hidden;
  }
  body {
    background: var(--backdrop);
    font-family: "Arimo", Arial, sans-serif;
    color: var(--ink);
    display: flex;
    align-items: center;
    justify-content: center;
    gap: 44px;
  }
  .card {
    width: 540px;
    height: 310px;
    border-bottom: 3px solid var(--edge);
    box-shadow: 0 14px 30px rgba(0,0,0,0.28);
    position: relative;
  }

  /* Info side */
  .card--info {
    background: var(--card-white);
    display: flex;
    align-items: center;
  }
  .card--info .brand {
    width: 250px;
    display: flex;
    justify-content: center;
  }
  .card--info .divider {
    width: 1px;
    height: 170px;
    background: var(--divider);
  }
  .contact {
    padding-left: 28px;
    font-size: 15px;
    line-height: 1.3;
  }
  .contact__name {
    font-weight: 700;
    font-size: 20px;
    letter-spacing: 0.5px;
    text-transform: uppercase;
  }
  .contact__name .first { color: var(--accent); }
  .contact__role { font-size: 15px; margin-bottom: 14px; }
  .contact__line {
    display: flex;
    align-items: center;
    gap: 8px;
  }
  .contact__line svg { width: 13px; height: 13px; flex: none; }
  .contact__line .hl { color: var(--accent); }
  .contact__address { margin-top: 14px; }

  /* Brand wordmark */
  .brand__mark {
    display: flex;
    align-items: center;
    gap: 10px;
  }
  .brand__square {
    width: 22px;
    height: 22px;
    background: var(--accent);
    flex: none;
  }
  .brand__name {
    font-weight: 700;
    color: var(--ink-logo);
    text-transform: uppercase;
    line-height: 1;
    font-size: 24px;
    letter-spacing: 1px;
  }
  .brand__name span { display: block; }
  .brand__name .sub { font-size: 16px; letter-spacing: 3px; margin-top: 5px; }

  /* Logo side */
  .card--logo {
    background: var(--card-grey);
    display: flex;
    align-items: center;
    justify-content: center;
  }
  .card--logo .brand__mark { gap: 18px; }
  .card--logo .brand__square { width: 44px; height: 44px; }
  .card--logo .brand__name { font-size: 52px; letter-spacing: 2px; }
  .card--logo .brand__name .sub { font-size: 32px; letter-spacing: 6px; margin-top: 10px; }
</style>
</head>
<body>

  <section class="card card--info" aria-label="Card back with contact details">
    <div class="brand">
      <div class="brand__mark">
        <div class="brand__square"></div>
        <div class="brand__name"><span>Keystone</span><span class="sub">Mechanical</span></div>
      </div>
    </div>
    <div class="divider"></div>
    <div class="contact">
      <p class="contact__name"><span class="first">Daniel</span> Harper</p>
      <p class="contact__role">Managing Director</p>
      <p class="contact__line">
        <svg viewBox="0 0 16 16" aria-hidden="true"><path fill="#f0842c" d="M3.6 1.5l2.3 2.6-1.3 1.8c.9 2 2.4 3.6 4.5 4.6l1.8-1.3 2.6 2.3-1.5 2.3C6.6 13.6 2.4 9.4 1.3 3z"/></svg>
        044-555 018 240
      </p>
      <p class="contact__line">
        <svg viewBox="0 0 16 16" aria-hidden="true"><rect x="1" y="3" width="14" height="10" fill="#f0842c"/><path d="M1 3l7 6 7-6" fill="none" stroke="#fff" stroke-width="1.4"/></svg>
        hello@keystonemech.com
      </p>
      <p class="contact__line">
        <svg viewBox="0 0 16 16" aria-hidden="true"><circle cx="8" cy="8" r="7" fill="#f0842c"/><path d="M1 8h14M8 1c-3 3.5-3 10.5 0 14M8 1c3 3.5 3 10.5 0 14" fill="none" stroke="#fff" stroke-width="1"/></svg>
        <span>www.<span class="hl">keystonemech</span>.com</span>
      </p>
      <p class="contact__address">87 Foundry Row, Suite 4<br>38117, Westbrook</p>
    </div>
  </section>

  <section class="card card--logo" aria-label="Card front with company name">
    <div class="brand__mark">
      <div class="brand__square"></div>
      <div class="brand__name"><span>Keystone</span><span class="sub">Mechanical</span></div>
    </div>
  </section>

</body>
</html>
```